Website for an interior designer

We need a new website for Rosa Lynn Thackery whose new business name is Rosa Lynn Thackery Interiors. She is a residential interior designer with a mix of modern and contemporary tastes. We are in the process of overhauling her website which is +15 years old and not an accurate reflection of her tastes. The uploaded photos are from some of the houses she has done as well as her logo(s). We would need a section for "About Us" that would have a paragraph of text and bullets showing services and a gallery for photos (~12 total, more to come). A contract page would be optional. The client likes the feel/look of this website: https://www.corvenhollowdesign.example/ but doesn't want to copy it exactly.

Target Market(s)

Upscale home owners

Industry/Entity Type

Interior Design

Coding

Coded - Design and coding required

Number of Pages Required

4 page

Colors

Designer to choose only greyscale colors for use in the design.

Requirements
Must have
• Home page, about us page, gallery page, contact us page.

```html
<!DOCTYPE html>
<html lang="en">
<head>
<meta charset="utf-8">
<title>Rosa Lynn Thackery Interiors</title>
<link href="https://fonts.googleapis.com/css2?family=Marcellus&family=Poppins:wght@400;500;600;700&family=Open+Sans:wght@400;600&display=swap" rel="stylesheet">
<style>
:root{
  --band:#b4b9b8;
  --band-light:#eceeed;
  --accent:#8c8c8c;
  --ink:#2a2a2a;
  --body:#5c5c5c;
  --button:#2f2f2f;
  --white:#ffffff;
  --deco-dark:#6e6e6e;
  --deco-mid:#a9a9a9;
}
*{margin:0;padding:0;box-sizing:border-box}
html,body{width:1200px;height:2832px;overflow:hidden;background:var(--white)}
body{position:relative;font-family:"Open Sans",Arial,sans-serif;color:var(--body)}
.abs{position:absolute}
.photo{position:absolute}
.btn{position:absolute;background:var(--button);color:var(--white);font-family:"Poppins",Arial,sans-serif;font-size:13px;font-weight:500;letter-spacing:1px;padding:0 20px;height:36px;line-height:36px;text-transform:uppercase;white-space:nowrap}
.section-title{font-family:"Marcellus",Georgia,serif;font-size:30px;font-weight:400;color:var(--ink);letter-spacing:1.5px;text-transform:uppercase;white-space:nowrap}
.icon{fill:var(--accent)}
.icon-line{fill:none;stroke:var(--accent)}

/* header */
.brand{left:120px;top:24px;width:200px;text-align:center}
.brand-dot{width:26px;height:26px;border-radius:50%;border:1px solid var(--ink);margin:0 auto 6px}
.brand-name{font-family:"Marcellus",Georgia,serif;font-size:14px;color:var(--ink);letter-spacing:1px;text-transform:uppercase;white-space:nowrap}
.brand-sub{font-family:"Marcellus",Georgia,serif;font-size:9px;letter-spacing:4px;color:var(--body);margin-top:3px}
.nav{left:532px;top:56px;display:flex;gap:46px;font-family:"Poppins",Arial,sans-serif;font-size:13px;font-weight:500;letter-spacing:1px;color:var(--ink)}
.nav .active{color:var(--accent)}

/* hero */
.hero-ring{left:372px;top:500px;width:200px;height:200px;border-radius:50%;background:var(--band-light)}
.hero-photo{left:640px;top:108px;width:560px;height:552px;
  background:radial-gradient(ellipse at 40% 75%,rgba(190,170,140,.55) 0%,rgba(190,170,140,0) 55%),
             linear-gradient(175deg,#f6f5f2 0%,#ebe8e2 50%,#d8d2c7 100%)}
.hero-kicker{left:140px;top:250px;font-family:"Poppins",Arial,sans-serif;font-size:12px;letter-spacing:2px;color:var(--body)}
.hero-title{left:140px;top:272px;font-family:"Poppins",Arial,sans-serif;font-weight:700;font-size:40px;line-height:56px;color:var(--ink);white-space:nowrap}
.hero-title span{color:var(--accent)}
.hero-btn{left:140px;top:400px}

/* about */
.about-band{left:0;top:800px;width:560px;height:360px;background:var(--band)}
.about-photo{left:0;top:840px;width:508px;height:468px;
  background:radial-gradient(ellipse at 30% 70%,rgba(255,255,255,.7) 0%,rgba(255,255,255,0) 50%),
             linear-gradient(165deg,#eeece7 0%,#d6d1c8 60%,#9a8d7d 100%)}
.about-title{left:608px;top:928px}
.about-text{left:608px;top:994px;width:540px;font-size:14.5px;line-height:27px}
.about-btn{left:608px;top:1184px}

/* services */
.services-band{left:640px;top:1392px;width:560px;height:328px;background:var(--band)}
.services-photo{left:692px;top:1460px;width:508px;height:452px;
  background:radial-gradient(ellipse at 55% 35%,rgba(255,255,255,.8) 0%,rgba(255,255,255,0) 50%),
             linear-gradient(170deg,#f1f2f2 0%,#d3d6d8 55%,#a1a5a8 100%)}
.services-title{left:140px;top:1506px}
.services-list{left:140px;top:1578px;list-style:none;font-size:14.5px;line-height:31px}
.services-list li::before{content:"";display:inline-block;width:5px;height:5px;border-radius:50%;background:var(--ink);margin:0 12px 3px 0}
.services-btn{left:140px;top:1824px}

/* gallery */
.gallery-band{left:0;top:2000px;width:1200px;height:260px;background:var(--band)}
.gallery-title{left:0;top:2074px;width:1200px;text-align:center;color:var(--white)}
.gallery-item{top:2164px;width:212px;height:256px}
.g1{left:140px;background:radial-gradient(ellipse at 50% 45%,#ffffff 0%,rgba(255,255,255,0) 55%),linear-gradient(170deg,#efeeeb,#c4bfb6)}
.g2{left:376px;background:radial-gradient(ellipse at 50% 60%,#f6f6f6 0%,rgba(246,246,246,0) 50%),linear-gradient(170deg,#e8e9ea,#85898d)}
.g3{left:612px;background:radial-gradient(ellipse at 45% 60%,#ffffff 0%,rgba(255,255,255,0) 50%),linear-gradient(170deg,#f0efec,#b2ada4)}
.g4{left:848px;background:radial-gradient(ellipse at 50% 70%,rgba(220,218,214,.8) 0%,rgba(220,218,214,0) 50%),linear-gradient(170deg,#dedcd8,#5f5b55)}
.deco-dark{left:20px;top:2372px;width:34px;height:88px;background:var(--deco-dark)}
.deco-mid{left:58px;top:2372px;width:30px;height:88px;background:var(--deco-mid)}
.gallery-btn{left:541px;top:2456px}

/* footer */
.foot-col{top:2570px;font-size:12.5px;line-height:22px}
.foot-head{font-family:"Marcellus",Georgia,serif;font-size:16px;color:var(--ink);letter-spacing:1px;text-transform:uppercase;margin-bottom:8px}
.foot-quick{left:140px}
.foot-links{list-style:none}
.foot-links li::before{content:"›";margin-right:8px;color:var(--ink)}
.foot-contact{left:360px}
.contact-row{display:flex;align-items:center;gap:10px}
.contact-row svg{flex:none}
.contact-name{color:var(--ink);font-weight:600}
.contact-address{padding-left:22px}
.foot-social{left:680px}
.social-row{display:flex;align-items:center;gap:10px;margin-bottom:8px}
.social-dot{width:22px;height:22px;border-radius:50%;background:var(--ink)}
.foot-mark{left:860px;top:2592px;width:200px;text-align:center;font-family:"Marcellus",Georgia,serif;color:var(--ink)}
.foot-mark .mark-name{font-size:24px;line-height:32px}
.foot-mark .mark-sub{font-size:11px;letter-spacing:5px;margin-top:6px}
.copyright{left:0;top:2800px;width:1200px;height:32px;background:var(--band);color:var(--white);font-size:11px;text-align:center;line-height:32px;letter-spacing:.5px}
</style>
</head>
<body>

<header>
  <div class="abs brand">
    <div class="brand-dot"></div>
    <div class="brand-name">Rosa Lynn Thackery</div>
    <div class="brand-sub">INTERIORS</div>
  </div>
  <nav class="abs nav">
    <span class="active">HOME</span><span>ABOUT US</span><span>SERVICES</span><span>GALLERY</span><span>CONTACT US</span>
  </nav>
</header>

<section class="hero">
  <div class="abs hero-ring"></div>
  <div class="photo hero-photo" role="img" aria-label="Bright living room with a wooden sofa, cushions, a white sideboard and framed art"></div>
  <div class="abs hero-kicker">WELCOME TO</div>
  <h1 class="abs hero-title">Best <span>Interior</span><br>Design For Your Family</h1>
  <div class="btn hero-btn">Contact Us Today</div>
</section>

<section class="about">
  <div class="abs about-band"></div>
  <div class="photo about-photo" role="img" aria-label="Open living room with white sofas, large windows and a fireplace"></div>
  <h2 class="abs section-title about-title">About Rosa Lynn Thackery</h2>
  <p class="abs about-text">Rosa Lynn Thackery has extensive experience in all aspects of interior design. She has worked on a wide array of residential and commercial projects in her hometown of Brookvale and across the United States. Rosa Lynn's taste can best be described as a sophisticated blend of modern and traditional styles that combine to create a clean, timeless space.</p>
  <div class="btn about-btn">Read More</div>
</section>

<section class="services">
  <div class="abs services-band"></div>
  <div class="photo services-photo" role="img" aria-label="White kitchen with a steel range hood, stove and marble counters"></div>
  <h2 class="abs section-title services-title">Our Services</h2>
  <ul class="abs services-list">
    <li>Concept Origination and Project Management</li>
    <li>Review of Proposed Plans for New Construction and Remodels</li>
    <li>Procurement of Furniture, Accents, Art, Fixtures and Fittings</li>
    <li>Selection of Paints, Finishes and Construction Materials</li>
    <li>Vendor Coordination and Recommendations</li>
    <li>Home Staging, Styling and Editing</li>
  </ul>
  <div class="btn services-btn">Read More</div>
</section>

<section class="gallery">
  <div class="abs gallery-band"></div>
  <h2 class="abs section-title gallery-title">Our Gallery</h2>
  <div class="photo gallery-item g1" role="img" aria-label="White spiral staircase in a bright hallway"></div>
  <div class="photo gallery-item g2" role="img" aria-label="Dining room with white chairs and a dark table"></div>
  <div class="photo gallery-item g3" role="img" aria-label="Curved white sofa in a sunlit lounge"></div>
  <div class="photo gallery-item g4" role="img" aria-label="Living room with a grey sectional and tall bookshelves"></div>
  <div class="abs deco-dark"></div>
  <div class="abs deco-mid"></div>
  <div class="btn gallery-btn">View All</div>
</section>

<footer>
  <div class="abs foot-col foot-quick">
    <div class="foot-head">Quick Links</div>
    <ul class="foot-links">
      <li>Home</li><li>About Us</li><li>Services</li><li>Gallery</li><li>Contact Us</li>
    </ul>
  </div>
  <div class="abs foot-col foot-contact">
    <div class="foot-head">Contact Details</div>
    <div class="contact-row">
      <svg width="12" height="14" viewBox="0 0 12 14"><path class="icon" d="M6 0a5 5 0 0 0-5 5c0 4 5 9 5 9s5-5 5-9a5 5 0 0 0-5-5zm0 7a2 2 0 1 1 0-4 2 2 0 0 1 0 4z"/></svg>
      <span class="contact-name">ROSA LYNN THACKERY</span>
    </div>
    <div class="contact-address">2140 Alder Court, Suite 3B<br>Brookvale, TX 77019</div>
    <div class="contact-row">
      <svg width="12" height="12" viewBox="0 0 12 12"><path class="icon" d="M2.5 0.5l2 2.5-1.2 1.5a7 7 0 0 0 4.2 4.2L9 7.5l2.5 2L10 11.5C5 11.5 0.5 7 0.5 2z"/></svg>
      <span>(555) 014-2297</span>
    </div>
    <div class="contact-row">
      <svg width="12" height="10" viewBox="0 0 12 10"><rect class="icon-line" x="0.5" y="0.5" width="11" height="9"/><path class="icon-line" d="M0.5 0.5L6 5.5 11.5 0.5"/></svg>
      <span>hello@rosalynnthackery.example</span>
    </div>
  </div>
  <div class="abs foot-col foot-social">
    <div class="foot-head">Follow Us</div>
    <div class="social-row"><span class="social-dot"></span><span>Pinecircle</span></div>
    <div class="social-row"><span class="social-dot"></span><span>Chirpline</span></div>
    <div class="social-row"><span class="social-dot"></span><span>Snapframe</span></div>
  </div>
  <div class="abs foot-mark">
    <div class="mark-name">Rosa Lynn<br>Thackery</div>
    <div class="mark-sub">INTERIORS</div>
  </div>
  <div class="abs copyright">Copyright © 2024 Rosa Lynn Thackery Interiors. All Rights Reserved.</div>
</footer>

</body>
</html>
```